Business Card Design Project

We're looking for a unique business card design that stands out from the rest, using the brand and logo we've already developed.
Two-sided design please.
Vantor Creative (www.vantorcreative.example.au) is a digitally-focused advertising agency that has produces results-driven campaigns. As a result, we'd like our business card to reflect our innovative approach.
Size, shape, orientation, etc, are all flexible (providing the print costs don't become ridiculous or we have to sit there with tiny scissors!).
Business card should include space for name, title, email, mobile, landline and address.

```html
<!DOCTYPE html>
<html lang="en">
<head>
<meta charset="utf-8">
<title>Vantor Creative — Business Card</title>
<link href="https://fonts.googleapis.com/css2?family=Roboto+Condensed:wght@400;700&display=swap" rel="stylesheet">
<style>
  :root {
    --orange: #f28a2e;
    --orange-soft: #f6b072;
    --orange-deep: #e6741a;
    --ink: #262626;
    --ink-soft: #555555;
    --muted: #9a9a9a;
    --paper: #ffffff;
    --backdrop: #ebe8e3;
  }
  * { box-sizing: border-box; margin: 0; padding: 0; }
  html, body { width: 1200px; height: 646px; overflow: hidden; }
  body {
    background: var(--backdrop);
    font-family: "Roboto Condensed", "Arial Narrow", sans-serif;
    color: var(--ink);
    position: relative;
  }
  .card {
    position: absolute;
    top: 168px;
    width: 540px;
    height: 310px;
    background: var(--paper);
    overflow: hidden;
    box-shadow: 0 2px 8px rgba(0,0,0,0.12);
  }
  .card--back { left: 50px; }
  .card--front { left: 610px; }

  /* Back side */
  .back-band { position: absolute; left: 0; top: 0; width: 100%; height: 120px; background: var(--orange); }
  .tagline {
    position: absolute; top: 12px; left: 0; width: 100%;
    text-align: center; font-weight: 700; font-size: 18px; color: var(--ink);
  }
  .loop-art {
    position: absolute; left: 70px; top: 46px; width: 400px; height: 222px;
    border-radius: 12px;
    background: linear-gradient(160deg, var(--ink-soft) 0%, var(--orange) 55%, var(--orange-soft) 100%);
  }
  .services {
    position: absolute; width: 170px; text-align: center;
    font-weight: 700; font-size: 16px; line-height: 1.3; color: var(--paper);
  }
  .services--left { left: 95px; top: 160px; }
  .services--right { left: 275px; top: 96px; }
  .back-web {
    position: absolute; bottom: 14px; left: 0; width: 100%;
    text-align: center; font-size: 12px; color: var(--muted); letter-spacing: .5px;
  }

  /* Front side */
  .front-band { position: absolute; left: 0; bottom: 0; width: 100%; height: 140px; background: var(--orange); }
  .brand {
    position: absolute; left: 0; top: 44px; width: 100%;
    display: flex; justify-content: center; align-items: center; gap: 12px;
  }
  .brand-dot { width: 20px; height: 20px; border-radius: 50%; background: var(--orange); }
  .brand-name { font-weight: 400; font-size: 50px; color: var(--ink); letter-spacing: 1px; }
  .person {
    position: absolute; left: 0; top: 118px; width: 100%; text-align: center;
    color: var(--ink); font-weight: 700; line-height: 1.15;
  }
  .person-name { font-size: 17px; text-transform: uppercase; }
  .person-title { font-size: 14px; font-weight: 400; }
  .address {
    position: absolute; right: 30px; top: 188px;
    display: flex; gap: 8px; color: var(--ink);
    font-weight: 700; font-size: 14px; line-height: 1.3;
  }
  .address svg { width: 14px; height: 18px; fill: var(--ink); flex: none; margin-top: 2px; }
  .contact {
    position: absolute; left: 34px; bottom: 16px;
    list-style: none; color: var(--paper); font-size: 15px; line-height: 1.4;
  }
  .contact li { display: flex; align-items: center; gap: 10px; }
  .contact svg { width: 13px; height: 13px; fill: var(--paper); flex: none; }
</style>
</head>
<body>

<section class="card card--back" aria-label="Business card back">
  <div class="back-band"></div>
  <h2 class="tagline">Advertising for the Digital Age</h2>
  <div class="loop-art" role="img" aria-label="Illustration of two looping arrows linking the two service groups"></div>
  <p class="services services--left">TV&amp;Radio<br>Social Media<br>Online Video</p>
  <p class="services services--right">Search Engine<br>Email Marketing<br>Banner&amp;Display Ads</p>
  <p class="back-web">www.vantorcreative.example.au</p>
</section>

<section class="card card--front" aria-label="Business card front">
  <div class="front-band"></div>

  <div class="brand">
    <span class="brand-dot"></span>
    <span class="brand-name">Vantor Creative</span>
  </div>

  <div class="person">
    <p class="person-name">Alex Carter</p>
    <p class="person-title">president</p>
  </div>

  <div class="address">
    <svg viewBox="0 0 16 20" aria-hidden="true"><path d="M8 0a6 6 0 0 0-6 6c0 4.5 6 14 6 14s6-9.5 6-14a6 6 0 0 0-6-6zm0 8.5A2.5 2.5 0 1 1 8 3.5a2.5 2.5 0 0 1 0 5z"/></svg>
    <p>Brisbane Head Office<br>4/27 Harlow St,<br>Ashgrove, Qld 4060</p>
  </div>

  <ul class="contact">
    <li><svg viewBox="0 0 14 14" aria-hidden="true"><path d="M3 1l2.2 2.6-1.1 1.6a8 8 0 0 0 4.7 4.7l1.6-1.1L13 11l-1.4 2C6.5 13 1 7.5 1 2.4z"/></svg>1300 555 018</li>
    <li><svg viewBox="0 0 14 14" aria-hidden="true"><path d="M4 0h6a1 1 0 0 1 1 1v12a1 1 0 0 1-1 1H4a1 1 0 0 1-1-1V1a1 1 0 0 1 1-1zm0 2v9h6V2z"/></svg>0400 555 271</li>
    <li><svg viewBox="0 0 14 14" aria-hidden="true"><path d="M0 3h14v8H0zm1 1v.4l6 3.6 6-3.6V4z"/></svg>yourname@vantorcreative.example.au</li>
  </ul>
</section>

</body>
</html>
```